lighting products eshop web site

We need a brand new ecommerce website (only psd files for the layout) , that will sell professional lighting products in Greek territory.
Please check the sister site www.lumena-shop.gr to get an idea of the products, they will be similar, actually like the products under the menu category "ΕΠΑΓΓΕΛΜΑΤΙΚΑ".
We would like the same philosophy as far as concern the menu structure, namely the menu categories/subcategories shall be actually the products
categories/subcategories, however the menu items shall be presented in a different, more sophisticated way. As far as concern the website layout, we need a minimal, elegant
and contemporary approach that will highlight the products in a perfect manner. We prefer the white color as the main website (background) color and discrete use of brand logo colors.
That is the main idea, awaiting your personal proposal according to the aforementioned requirements
Technically speaking we use bootstrap framework in terms of design meaning 12cols with max width 1170px.
The website will be a joomla - virtuemart website

For images please use some from lumena-shop.gr
For text use any text - just to show me the space.

Industry/Entity Type

It Professional

Number of Pages Required

3 page

Font styles to use
Sans Serif

Colors
00a990
ec1f27

Requirements
Must have
• I need 4 psd pages for the website
• 1. Start page
• 2. Category page
• 3. Product details page
• 4. blog page
Nice to have
• leave designer to choose the best

```html
<!DOCTYPE html>
<html lang="en">
<head>
<meta charset="utf-8">
<title>Lumena – Hanging Lights</title>
<link href="https://fonts.googleapis.com/css2?family=Montserrat:wght@400;600;700&family=Open+Sans:wght@400;600;700&display=swap" rel="stylesheet">
<style>
:root{
  --red:#ec1f27;
  --teal:#00a990;
  --orange:#f39200;
  --ink:#333;
  --muted:#8a8a8a;
  --line:#e4e4e4;
  --soft:#f3f3f3;
  --banner:#ecebe6;
  --footer:#1e1e1e;
  --footer-2:#2b2b2b;
  --thumb:#f1f1f1;
}
*{box-sizing:border-box;margin:0;padding:0}
html,body{width:692px;height:1200px;overflow:hidden;background:#fff}
body{font-family:"Open Sans",Arial,sans-serif;color:var(--ink);font-size:6px}
.page{position:relative;width:692px;height:1200px;overflow:hidden}

.topbar{height:18px;background:var(--soft);display:flex;align-items:center;justify-content:space-between;padding:0 50px;font-size:5.5px;color:var(--muted)}
.topbar .offer{display:flex;align-items:center;gap:5px}
.topbar .dot{width:8px;height:8px;background:var(--red);border-radius:1px}

.header{height:38px;display:flex;align-items:center;justify-content:center;position:relative}
.logo{font-family:"Montserrat",sans-serif;font-weight:600;font-size:17px;letter-spacing:3px;color:var(--teal)}
.header-actions{position:absolute;right:50px;top:11px;display:flex;gap:4px}
.icon-btn{width:16px;height:16px;background:var(--red);display:flex;align-items:center;justify-content:center;border-radius:1px}
.nav{height:22px;display:flex;justify-content:center;gap:16px;align-items:center;font-family:"Montserrat",sans-serif;font-weight:700;font-size:5.5px;border-bottom:1px solid var(--line)}
.nav a{color:var(--ink);text-decoration:none}

.breadcrumb{position:absolute;top:98px;left:50px;font-size:5.5px;color:var(--muted)}
.breadcrumb b{color:var(--ink);font-weight:600}

.sidebar{position:absolute;top:116px;left:50px;width:135px}
.box{border:1px solid var(--line);margin-bottom:12px}
.box-title{background:var(--red);color:#fff;font-family:"Montserrat",sans-serif;font-weight:700;font-size:6.5px;padding:6px 8px}
.box-body{padding:8px}
.label{font-weight:700;font-size:5.5px;margin:6px 0 5px;text-transform:uppercase}
.cat{font-size:5.5px;color:var(--muted);display:flex;gap:4px;align-items:center}
.check{width:5px;height:5px;border:1px solid #bbb;display:inline-block}
.price-row{display:flex;gap:4px;align-items:center}
.price-row span{border:1px solid var(--line);padding:2px 6px;font-size:5px;color:var(--muted)}
.price-row .go{background:var(--red);color:#fff;border-color:var(--red)}
.slider{position:relative;height:2px;background:#ddd;margin:12px 2px 10px}
.slider i{position:absolute;top:-3px;width:8px;height:8px;border-radius:50%;border:1px solid #999;background:#fff}
.list li{list-style:none;font-size:5.5px;color:var(--muted);display:flex;gap:4px;align-items:center;margin-bottom:4px}
.swatches{display:grid;grid-template-columns:repeat(4,1fr);gap:4px 6px}
.sw{display:flex;align-items:center;gap:3px;font-size:5px;color:var(--muted)}
.sw i{width:9px;height:9px;display:inline-block}
.seller{display:flex;gap:6px;padding:6px 0;border-bottom:1px solid var(--line)}
.seller:last-child{border-bottom:0}
.seller .thumb{width:34px;height:34px;background:var(--thumb)}
.seller p{font-size:5.5px;line-height:1.5}
.stars{color:var(--orange);font-size:5.5px;letter-spacing:.5px}
.price{color:var(--red);font-weight:700;font-size:7px}

.main{position:absolute;top:116px;left:198px;width:447px}
.banner{height:137px;background:var(--banner);display:flex;padding:18px}
.banner-text{width:190px}
.banner h1{font-family:"Montserrat",sans-serif;font-weight:700;font-size:14px;color:var(--orange);letter-spacing:1px;margin-bottom:8px}
.banner p{font-size:5.5px;line-height:1.6;color:#666}
.banner-img{margin-left:auto;width:160px;height:100px;background:radial-gradient(#fbfbfa,#dcdad3)}
.toolbar{display:flex;align-items:center;gap:4px;margin:24px 0 8px;font-size:5px;color:var(--muted);border-bottom:1px solid var(--line);padding-bottom:6px}
.toolbar .view{width:10px;height:10px;background:var(--red)}
.toolbar .view.off{background:#ccc}
.toolbar .sort{margin-left:100px;display:flex;gap:6px;align-items:center}
.toolbar .sort span{border:1px solid var(--line);padding:1px 8px}
.grid{display:grid;grid-template-columns:repeat(4,1fr);gap:12px 10px}
.card{position:relative;border:1px solid var(--line);padding:5px;text-align:left}
.card .thumb{height:100px;background:var(--thumb);margin-bottom:5px}
.card .tag{position:absolute;top:5px;left:5px;background:var(--orange);color:#fff;font-size:4.5px;font-weight:700;padding:1px 4px}
.card .name{font-size:5.5px;margin:2px 0;color:#555}
.card .old{color:var(--muted);text-decoration:line-through;font-size:5px;margin-left:3px;font-weight:400}

.footer{position:absolute;top:930px;left:0;width:692px;height:270px;background:linear-gradient(var(--footer),var(--footer-2))}
.footer-nav{display:flex;justify-content:center;gap:20px;padding:12px 0;font-family:"Montserrat",sans-serif;font-weight:700;font-size:5px;color:#ddd;border-bottom:1px solid #3a3a3a}
.footer-body{height:230px;background:linear-gradient(#262626,#3a3a3a 60%,#2a2a2a);display:flex;flex-direction:column;align-items:center;padding-top:40px}
.footer .logo{font-size:15px}
.footer-body p{font-size:5.5px;color:#aaa;margin-top:8px;text-align:center;line-height:1.6}
.social{display:flex;gap:6px;margin-top:18px}
.social i{width:13px;height:13px;border:1px solid #888;border-radius:50%;display:block}
.copy{margin-top:18px!important}
.copy b{color:var(--red);font-weight:600}
.cards{display:flex;gap:4px;margin-top:10px}
.cards i{width:16px;height:10px;background:#ddd;border-radius:1px;display:block}
</style>
</head>
<body>
<div class="page">
  <div class="topbar">
    <div class="offer"><span class="dot"></span>OFFERS UP TO 30% OFF · +30 210 000 4321</div>
    <div>hello@lumena-shop.gr</div>
  </div>
  <header class="header">
    <div class="logo">LUMENA</div>
    <div class="header-actions">
      <span class="icon-btn"><svg width="8" height="8" viewBox="0 0 10 10"><circle cx="4" cy="4" r="3" fill="none" stroke="#fff" stroke-width="1.3"/><line x1="6.3" y1="6.3" x2="9" y2="9" stroke="#fff" stroke-width="1.3"/></svg></span>
      <span class="icon-btn"><svg width="8" height="8" viewBox="0 0 10 10"><path d="M1 2h1.5l1.3 5h4.5L9 3.5H3" fill="none" stroke="#fff" stroke-width="1.1"/><circle cx="4.3" cy="8.7" r=".8" fill="#fff"/><circle cx="7.7" cy="8.7" r=".8" fill="#fff"/></svg></span>
    </div>
  </header>
  <nav class="nav">
    <a>HANGING</a><a>DESK</a><a>FLOOR</a><a>WALL</a><a>SPOT</a><a>OUTDOOR</a><a>FANS</a><a>PROFESSIONAL</a><a>COMPANIES</a>
  </nav>

  <div class="breadcrumb">Home / <b>Hanging</b></div>

  <aside class="sidebar">
    <div class="box">
      <div class="box-title">SHOP BY</div>
      <div class="box-body">
        <div class="label">Category</div>
        <div class="cat"><span class="check"></span>Hanging (27)</div>
        <div class="label" style="margin-top:40px">Price</div>
        <div class="price-row"><span>100</span>–<span>500</span><span class="go">FILTER</span></div>
        <div class="slider"><i style="left:-2px"></i><i style="left:45%"></i></div>
        <div class="label">Manufacturer</div>
        <ul class="list">
          <li><span class="check"></span>Luce Atelier (12)</li>
          <li><span class="check"></span>Nordlys (8)</li>
          <li><span class="check"></span>Arcadia (5)</li>
          <li><span class="check"></span>Vetro Lux (4)</li>
          <li><span class="check"></span>Brightline (3)</li>
        </ul>
        <div class="label">Colour</div>
        <div class="swatches">
          <div class="sw"><i style="background:#111"></i>Black</div>
          <div class="sw"><i style="background:#2b4fa0"></i>Blue</div>
          <div class="sw"><i style="background:#fff;border:1px solid #ccc"></i>White</div>
          <div class="sw"><i style="background:#7a4a20"></i>Brown</div>
          <div class="sw"><i style="background:#2ec4e6"></i>Cyan</div>
          <div class="sw"><i style="background:#c8a048"></i>Gold</div>
          <div class="sw"><i style="background:#999"></i>Grey</div>
        </div>
      </div>
    </div>
    <div class="box">
      <div class="box-title">BEST SELLER</div>
      <div class="box-body" style="padding:2px 8px">
        <div class="seller"><div class="thumb" role="img" aria-label="Pendant lamp product photo"></div><p>Drop pendant<br><span class="stars">★★★★★</span><br><span class="price">€550.00</span></p></div>
        <div class="seller"><div class="thumb" role="img" aria-label="Crystal chandelier product photo"></div><p>Crystal chandelier<br><span class="stars">★★★★★</span><br><span class="price">€500.00</span></p></div>
        <div class="seller"><div class="thumb" role="img" aria-label="Glass pendant product photo"></div><p>Glass pendant<br><span class="stars">★★★★☆</span><br><span class="price">€820.00</span></p></div>
        <div class="seller"><div class="thumb" role="img" aria-label="Dome lamp product photo"></div><p>Dome lamp black<br><span class="stars">★★★★★</span><br><span class="price">€995.00</span></p></div>
      </div>
    </div>
  </aside>

  <main class="main">
    <section class="banner">
      <div class="banner-text">
        <h1>HANGING</h1>
        <p>Elegant pendant lights and chandeliers for every room. Explore refined shapes, warm glass and metal finishes chosen to bring soft, balanced light to homes, shops and professional spaces alike.</p>
      </div>
      <div class="banner-img" role="img" aria-label="Crystal chandelier photograph"></div>
    </section>

    <div class="toolbar">
      <span class="view"></span><span class="view off"></span>
      <div class="sort">Sort By <span>Position ▾</span> Show <span>12 ▾</span></div>
    </div>

    <div class="grid">
      <div class="card"><span class="tag">SALE</span><div class="thumb" role="img" aria-label="Triple pendant lamp photo"></div><div class="stars">★★★★★</div><div class="name">Trio bulb line</div><div class="price">€150.00<span class="old">€200.00</span></div></div>
      <div class="card"><div class="thumb" role="img" aria-label="Gold chandelier photo"></div><div class="stars">★★★★★</div><div class="name">Gilded candle crown</div><div class="price">€560.00</div></div>
      <div class="card"><div class="thumb" role="img" aria-label="Tulip chandelier photo"></div><div class="stars">★★★★★</div><div class="name">Tulip glass arms</div><div class="price">€150.00</div></div>
      <div class="card"><span class="tag">SALE</span><div class="thumb" role="img" aria-label="Black dome pendant photo"></div><div class="stars">★★★★★</div><div class="name">Dark dome pendant</div><div class="price">€1,000.00</div></div>

      <div class="card"><div class="thumb" role="img" aria-label="Brass pendant photo"></div><div class="stars">★★★★★</div><div class="name">Brass bell shade</div><div class="price">€1,210.00</div></div>
      <div class="card"><div class="thumb" role="img" aria-label="Black cone pendant photo"></div><div class="stars">★★★★★</div><div class="name">Cone pendant matte</div><div class="price">€150.00</div></div>
      <div class="card"><div class="thumb" role="img" aria-label="Crystal chandelier photo"></div><div class="stars">★★★★★</div><div class="name">Crystal drop ring</div><div class="price">€585.00</div></div>
      <div class="card"><div class="thumb" role="img" aria-label="Linear pendant bar photo"></div><div class="stars">★★★★★</div><div class="name">Linear bar four</div><div class="price">€150.00</div></div>

      <div class="card"><span class="tag">SALE</span><div class="thumb" role="img" aria-label="Blue pendant lamp photo"></div><div class="stars">★★★★★</div><div class="name">Azure glass pendant</div><div class="price">€150.00<span class="old">€190.00</span></div></div>
      <div class="card"><div class="thumb" role="img" aria-label="Three glass pendants photo"></div><div class="stars">★★★★★</div><div class="name">Clear globe trio</div><div class="price">€150.00</div></div>
      <div class="card"><div class="thumb" role="img" aria-label="Gold dome pendant photo"></div><div class="stars">★★★★★</div><div class="name">Gold dome classic</div><div class="price">€150.00<span class="old">€210.00</span></div></div>
      <div class="card"><span class="tag">SALE</span><div class="thumb" role="img" aria-label="Black industrial pendant photo"></div><div class="stars">★★★★★</div><div class="name">Loft metal shade</div><div class="price">€1,250.00</div></div>
    </div>

    <div class="toolbar" style="margin-top:18px">
      <span class="view"></span><span class="view off"></span>
      <div class="sort">Sort By <span>Position ▾</span> Show <span>12 ▾</span></div>
    </div>
  </main>

  <footer class="footer">
    <div class="footer-nav">
      <span>COMPANY</span><span>SHOP</span><span>CORPORATE CUSTOMERS</span><span>DATA PROTECTION</span><span>TERMS OF USE</span><span>PAYMENT METHODS</span><span>SHIPPING METHODS</span><span>RETURN POLICY</span><span>CONTACT US</span>
    </div>
    <div class="footer-body" role="img" aria-label="Dark aerial photograph of the showroom building">
      <div class="logo">LUMENA</div>
      <p>Professional lighting for homes and businesses across Greece<br>Athens showroom · Mon–Sat 09:00–20:00</p>
      <div class="social"><i></i><i></i><i></i><i></i><i></i></div>
      <p class="copy">© 2016 lumena-shop.gr. All Rights Reserved. Designed by <b>Studio</b></p>
      <div class="cards"><i></i><i></i><i></i><i></i><i></i></div>
    </div>
  </footer>
</div>
</body>
</html>
```